INTERNATIONAL SPEAKING BUSINESS FOR WOMEN NEEDS A BROCHURE DESIGN

HEARTHSTONE CIRCLE IS AN INTERNATIONAL FEMALE NETWORK PROVIDING ITS MEMBERS THE UK'S NUMBER ONE RELATIONSHIP SEMINAR FOR WOMEN.
WE ARE ABOUT TO GO LIVE AGAIN AFTER 18 MONTHS AND ONE OF OUR OFFERINGS AT THIS LIVE EVENT, IS OUR BONDWISE WORKSHOP TRACK - AND THIS IS WHERE YOU COME IN :)
IM LOOKING FOR AN ELEGANT, EASY AND WARM TO THE EYE BROCHURE WHICH CAPTURES SOME OF OUR BEST TESTIMONIALS AND CLIENTS. WE HAVE THE LOGO, THE IMAGES AND THE COPY . WE JUST NEED YOUR AMAZING CREATIVE TALENT AND SKILL TO PUT IT ALL TOGETHER TO LOOK ELEGANT AND PROFESSIONAL, YET WELCOMING AND INSPIRING.
OUR IDEAL CLIENT IS A SINGLE, SUCCESSFUL, PROFESSIONAL WOMAN WANTING TO FIND A SOLUTION TO HER RELATIONSHIP CHALLENGES. SHE WANTS TO LET GO OF HER FEARS OF PAST RELATIONSHIPS AND ALIGN WITH AN AMAZING RELATIONSHIP. OUR AIM WITH THE BROCHURE IS TO SHOW THEM WHAT WE DO, HOW WE DO IT AND HOW OUR EXISTING CLIENTS HAVE ALREADY DONE THIS.
THIS IS JUST ONE OF MANY CREATIVE WORKS NEEDED TO BE CARRIED OUT OVER THESE NEXT FEW WEEKS
SO WE ARE LOOKING FOR OUR IDEAL CREATIVE PARTNER ! HOPING TO FIND YOU HERE ;)
hearthstonecircle-example.com
professional, successful women between 30 and 65 looking to resolve their relationship problems
Speaking Business/ Seminars / webinars/ Relationships Coaching for Women
- Similar to logo and website hearthstonecircle-example.com

```html
<!DOCTYPE html>
<html lang="en">
<head>
<meta charset="utf-8">
<title>Hearthstone Circle – Brochure</title>
<link rel="stylesheet" href="https://fonts.googleapis.com/css2?family=Oswald:wght@400;500;600&family=Barlow:ital,wght@0,400;0,500;0,700;1,400;1,500&display=swap">
<style>
  :root {
    --stage: #2a2a2b;
    --paper: #ffffff;
    --pink: #e0457b;
    --pink-deep: #c22f66;
    --berry: #b3245c;
    --berry-dark: #7d1f47;
    --blush: #fbe9f0;
    --grey: #8f8f96;
    --grey-light: #a6a6ad;
    --ink: #2d2a2e;
    --body-text: #5c5860;
    --heading: "Oswald", "Arial Narrow", sans-serif;
    --text: "Barlow", "Helvetica Neue", sans-serif;
  }
  * { box-sizing: border-box; margin: 0; padding: 0; }
  html, body { width: 913px; height: 1200px; overflow: hidden; }
  body { background: var(--stage); font-family: var(--text); color: var(--ink); position: relative; }

  .spread { position: absolute; left: 56px; width: 800px; height: 566px; display: flex; box-shadow: 0 18px 40px rgba(0,0,0,.45); }
  .spread--outer { top: 22px; }
  .spread--inner { top: 612px; }
  .page { position: relative; width: 400px; height: 566px; overflow: hidden; background: var(--paper); }

  /* Back cover */
  .back-cover__photo { position: absolute; inset: 0; background: radial-gradient(ellipse at 65% 40%, #e24a7e 0%, #c12d64 45%, #9a1f50 100%); }
  .back-cover__offer { position: absolute; left: 22px; top: 38px; width: 178px; height: 262px; background: rgba(110,26,62,.82); padding: 20px 16px; color: #fff; }
  .back-cover__offer h2 { font-family: var(--text); font-weight: 500; font-size: 17px; line-height: 1.08; letter-spacing: .3px; padding-bottom: 8px; border-bottom: 1px solid rgba(255,255,255,.8); }
  .back-cover__label { font-size: 11px; margin-top: 8px; }
  .back-cover__price { font-size: 19px; font-weight: 500; line-height: 1.05; }
  .back-cover__offer p.small { font-size: 6.6px; line-height: 1.45; margin-top: 8px; }
  .contact { position: absolute; left: 112px; top: 440px; color: #fff; }
  .contact h3 { font-family: var(--heading); font-weight: 500; font-size: 19px; letter-spacing: .5px; margin-bottom: 6px; }
  .contact li { list-style: none; display: flex; align-items: center; gap: 7px; font-size: 10px; line-height: 1.6; }
  .contact svg { width: 11px; height: 11px; flex: none; }

  /* Front cover */
  .brand { position: absolute; left: 24px; top: 24px; display: flex; align-items: center; gap: 12px; }
  .brand__dot { width: 34px; height: 34px; border-radius: 50%; background: var(--pink); }
  .brand__name { font-family: var(--heading); font-weight: 600; font-size: 24px; color: var(--pink); letter-spacing: .3px; line-height: 1; }
  .brand__track { font-family: var(--text); font-size: 9.5px; letter-spacing: 2.2px; color: var(--grey); margin-top: 4px; }
  .rule { position: absolute; left: 0; width: 400px; height: 3px; background: var(--pink); }
  .rule--top { top: 84px; }
  .photo { position: absolute; }
  .photo--stage { left: 18px; top: 98px; width: 108px; height: 98px; background: linear-gradient(160deg, #dfe2ea, #6b7597 60%, #2c3350); }
  .photo--audience { left: 18px; top: 202px; width: 108px; height: 104px; background: linear-gradient(180deg, #c8c9cf, #7a6f6c 60%, #3b302e); }
  .photo--speaker { left: 132px; top: 98px; width: 268px; height: 208px; background: linear-gradient(135deg, #c9856a, #8a4c36 50%, #3e2620); }
  .front-cover__wave { position: absolute; left: 0; top: 300px; width: 400px; height: 266px; }
  .headline { position: absolute; left: 30px; top: 336px; font-family: var(--heading); font-weight: 600; font-size: 29px; line-height: 1.12; color: var(--pink); }
  .headline__rule { position: absolute; left: 30px; top: 408px; width: 290px; height: 2px; background: var(--pink); }
  .subline { position: absolute; left: 30px; top: 418px; font-family: var(--heading); font-size: 13.5px; color: var(--grey); line-height: 1.35; }

  /* Inner left */
  .intro-band { position: absolute; left: 0; top: 0; width: 400px; height: 90px; }
  .intro-band__text { position: absolute; left: 24px; top: 16px; width: 350px; color: #fff; font-style: italic; font-size: 8.4px; line-height: 1.45; }
  .included { position: absolute; left: 24px; top: 92px; width: 360px; }
  .section-title { font-style: italic; font-weight: 500; color: var(--pink); font-size: 12px; }
  .included ol { margin: 5px 0 0 22px; font-style: italic; font-weight: 700; font-size: 7.8px; line-height: 1.55; }
  .info-row { position: absolute; left: 0; top: 148px; width: 400px; height: 108px; display: flex; }
  .about { width: 186px; background: var(--pink); color: #fff; padding: 14px 16px; }
  .about h3, .fit h3 { font-style: italic; font-weight: 500; font-size: 12px; margin-bottom: 8px; }
  .about p, .fit p { font-style: italic; font-size: 6.8px; line-height: 1.45; }
  .fit { flex: 1; background: var(--grey-light); color: #fff; padding: 12px 16px; }
  .learn { position: absolute; left: 24px; top: 274px; width: 350px; }
  .learn ul { list-style: none; margin-top: 8px; }
  .learn li { display: flex; gap: 7px; font-weight: 700; font-style: italic; font-size: 8.2px; line-height: 1.35; margin-bottom: 5px; color: var(--ink); }
  .learn svg { width: 9px; height: 9px; flex: none; margin-top: 1px; }
  .inner-wave { position: absolute; left: 0; bottom: 0; width: 400px; height: 190px; }
  .web { position: absolute; left: 100px; bottom: 44px; font-weight: 700; font-size: 11px; color: var(--grey); letter-spacing: .3px; }

  /* Inner right */
  .stories-wave { position: absolute; inset: 0; }
  .stories { position: absolute; left: 18px; top: 26px; width: 366px; list-style: none; }
  .story { display: flex; gap: 12px; height: 86px; }
  .story__photo { width: 62px; height: 70px; flex: none; background: linear-gradient(160deg, #d9c4b6, #9c7e6f 65%, #5a463d); }
  .story__name { font-weight: 700; font-size: 11px; color: var(--pink); line-height: 1.2; }
  .story__role { font-weight: 500; }
  .story__quote { font-size: 7px; line-height: 1.45; color: var(--body-text); margin-top: 3px; }
</style>
</head>
<body>

<section class="spread spread--outer" aria-label="Outer spread">
  <article class="page back-cover">
    <div class="back-cover__photo" role="img" aria-label="Photo of the seminar host smiling on stage, tinted magenta"></div>
    <div class="back-cover__offer">
      <h2>DON'T LET TODAY<br>FINISH HERE.</h2>
      <p class="back-cover__label">Subscription:</p>
      <p class="back-cover__price">£200 a month</p>
      <p class="small">Register today and get the first month's worth TODAY. Tomorrow, wake up and watch half a day of the most powerful content for relationships out there. That's half a day of advanced content for only £200.</p>
      <p class="small">If at any point you wish to cancel your subscription, just give us 30 days notice.</p>
    </div>
    <div class="contact">
      <h3>CONTACT US:</h3>
      <ul>
        <li><svg viewBox="0 0 12 12" fill="none" stroke="#fff" stroke-width="1"><path d="M3 1.5l2 2.5-1.2 1.2a7 7 0 003 3L8 7l2.5 2-1.2 1.5C5 10 2 7 1.5 3z"/></svg>+44 20 7946 0123</li>
        <li><svg viewBox="0 0 12 12" fill="none" stroke="#fff" stroke-width="1"><rect x="1" y="3" width="10" height="7"/><path d="M1 3l5 4 5-4"/></svg>contact@hearthstonecircle-example.com</li>
        <li><svg viewBox="0 0 12 12" fill="none" stroke="#fff" stroke-width="1"><circle cx="6" cy="6" r="5"/><path d="M1 6h10M6 1c-3 3-3 7 0 10M6 1c3 3 3 7 0 10"/></svg>www.hearthstonecircle-example.com</li>
      </ul>
    </div>
  </article>

  <article class="page front-cover">
    <svg class="front-cover__wave" viewBox="0 0 400 266" preserveAspectRatio="none" aria-hidden="true">
      <path d="M0 12 Q200 -6 400 10 V266 H0Z" fill="#fff"/>
      <path d="M0 150 C90 120 170 190 260 150 S380 110 400 130 V266 H0Z" fill="var(--blush)"/>
      <path d="M0 12 Q200 -6 400 10" stroke="var(--pink)" stroke-width="3" fill="none"/>
    </svg>
    <div class="brand">
      <span class="brand__dot"></span>
      <div>
        <div class="brand__name">HEARTHSTONE CIRCLE</div>
        <div class="brand__track">BONDWISE WORKSHOP TRACK</div>
      </div>
    </div>
    <div class="rule rule--top"></div>
    <div class="photo photo--stage" role="img" aria-label="Photo of the host presenting on stage in blue"></div>
    <div class="photo photo--audience" role="img" aria-label="Photo of the seminar audience facing the stage"></div>
    <div class="photo photo--speaker" role="img" aria-label="Photo of the host speaking with energy in front of seating"></div>
    <h1 class="headline">UK's #1 Relationship<br>Seminar For Women Only</h1>
    <div class="headline__rule"></div>
    <p class="subline">With Lena Marlow: #1 Best-selling Author of<br>"Rise And Unfold"</p>
  </article>
</section>

<section class="spread spread--inner" aria-label="Inner spread">
  <article class="page programme">
    <svg class="intro-band" viewBox="0 0 400 90" preserveAspectRatio="none" aria-hidden="true">
      <path d="M0 0H400V60 Q200 90 0 78Z" fill="var(--pink)"/>
    </svg>
    <p class="intro-band__text">Immerse yourself with a group of likeminded individuals in a weekly masterclass and get absorbed in some of the most senior relationships content that's changing the lives of thousands of women internationally.</p>
    <div class="included">
      <h3 class="section-title">What's Included:</h3>
      <ol>
        <li>Receive full access to the Bondwise Workshop Track (once a week)</li>
        <li>Gain full access to the network via our private members' forum.</li>
      </ol>
    </div>
    <div class="info-row">
      <div class="about">
        <h3>About The Masterclass:</h3>
        <p>Immerse yourself for one hour a week with like-minded individuals from the comfort and safety of your own home. Mondays 7pm-8pm</p>
      </div>
      <div class="fit">
        <h3>Is this programme for me?</h3>
        <p>If you wish to join one of the UK's Top Female Networks for a Life Changing Year but the unlimited programme is out of budget, then the Masterclass programme is for you. Give yourself that step in between. We've packaged it up so that you can afford it!</p>
      </div>
    </div>
    <svg class="inner-wave" viewBox="0 0 400 190" preserveAspectRatio="none" aria-hidden="true">
      <path d="M0 60 C100 20 200 90 300 50 S390 30 400 40 V190 H0Z" fill="var(--blush)"/>
    </svg>
    <div class="learn">
      <h3 class="section-title">What will I learn/ get from the programme?</h3>
      <ul>
        <li><svg viewBox="0 0 10 10" fill="none" stroke="var(--pink)" stroke-width="1"><rect x=".5" y=".5" width="9" height="9"/><path d="M2.5 5l2 2 3.5-4"/></svg>Weekly opportunity to have all your burning relationship questions answered</li>
        <li><svg viewBox="0 0 10 10" fill="none" stroke="var(--pink)" stroke-width="1"><rect x=".5" y=".5" width="9" height="9"/><path d="M2.5 5l2 2 3.5-4"/></svg>Immerse with a powerful network of like-minded women and learn even more</li>
        <li><svg viewBox="0 0 10 10" fill="none" stroke="var(--pink)" stroke-width="1"><rect x=".5" y=".5" width="9" height="9"/><path d="M2.5 5l2 2 3.5-4"/></svg>Tools to help you overcome past relationship wounds and patterns</li>
        <li><svg viewBox="0 0 10 10" fill="none" stroke="var(--pink)" stroke-width="1"><rect x=".5" y=".5" width="9" height="9"/><path d="M2.5 5l2 2 3.5-4"/></svg>Deepen your understanding of self-mastery on route to relationship Mastery</li>
      </ul>
    </div>
    <p class="web">www.hearthstonecircle-example.com</p>
  </article>

  <article class="page testimonials">
    <svg class="stories-wave" viewBox="0 0 400 566" preserveAspectRatio="none" aria-hidden="true">
      <path d="M240 0 C300 40 340 20 400 30 V0Z" fill="var(--blush)"/>
      <path d="M0 470 C120 430 250 520 400 480 V566 H0Z" fill="var(--blush)"/>
    </svg>
    <ul class="stories">
      <li class="story"><div class="story__photo" role="img" aria-label="Portrait of member Lucia"></div><div><p class="story__name">Lucia Brennan, <span class="story__role">34, Missing and Exploitation Coordinator.</span></p><p class="story__quote">I joined the circle to heal what I had been carrying for years. Each week gave me a new lens on love and on myself.</p></div></li>
      <li class="story"><div class="story__photo" role="img" aria-label="Portrait of member Helen"></div><div><p class="story__name">Helen Marsh, <span class="story__role">63, Midwife Labour Ward.</span></p><p class="story__quote">Honestly I didn't know how this would help, but the tools and the community helped me let go and truly open up again.</p></div></li>
      <li class="story"><div class="story__photo" role="img" aria-label="Portrait of member Sofia"></div><div><p class="story__name">Sofia Keller, <span class="story__role">39, Receptionist for Adult Mental Health</span></p><p class="story__quote">I feel so lucky to have found this group of amazing women. My thoughts, emotions and mindset have changed for the better.</p></div></li>
      <li class="story"><div class="story__photo" role="img" aria-label="Portrait of member Carmen"></div><div><p class="story__name">Carmen, <span class="story__role">42, Hairstylist</span></p><p class="story__quote">The sessions are a fantastic way of building on each lesson during the week. I now approach dating with calm and courage.</p></div></li>
      <li class="story"><div class="story__photo" role="img" aria-label="Portrait of member Maya"></div><div><p class="story__name">Maya Durant, <span class="story__role">33, Senior Customer Success Manager</span></p><p class="story__quote">These classes are the highlight of my week. I finally see my patterns clearly and I am ready to love myself first.</p></div></li>
      <li class="story"><div class="story__photo" role="img" aria-label="Portrait of member Valeria"></div><div><p class="story__name">Valeria Ortega, <span class="story__role">38, Director of Luxury Sales</span></p><p class="story__quote">The series is my most important weekly date with myself. Hearing other members' journeys inspires me to keep growing.</p></div></li>
    </ul>
  </article>
</section>

</body>
</html>
```